Tallowfern Studio business cards

We are a new company based in New Zealand. We Specialize in High end Luxury Residential Architecture.

Every home is bespoke and is designed to each clients individual requirements and needs.

I like to design buildings that inspire people through light and form while offering a high level of comfort and usability.

Lines of sight, proportion and balance are fundamental to the spaces I create.
Updates

August 5th is current deadline - Today's date is the 13th of August.

Target Market(s)

New Zealanders who want a custom individual home design, typically 30-65 year old males and females

Industry/Entity Type

Architecture

Contact Information for Business Card

Director - Derek Holloway
Contact Number - 0274619037
Email - info@tallowfernstudio.co.nz
Webstie - www.tallowfernstudio.co.nz
Social Media - @tallowfernstudio

Font styles to use
Sans Serif

Requirements
Must have
• Logo (Both Sides)
Website
Email
Contact Number
Social Media

Nice to have
• Texture
Should not have
• More than 3 colours - typically I would've thought 2 would be good to match the logo.

```html
<!DOCTYPE html>
<html lang="en">
<head>
<meta charset="utf-8">
<title>Tallowfern Studio – Business Cards</title>
<link href="https://fonts.googleapis.com/css2?family=Open+Sans:wght@400;700&display=swap" rel="stylesheet">
<style>
  :root {
    --backdrop: #8b8b8b;
    --card: #e5e5e7;
    --ink: #2f2f31;
    --ink-strong: #111112;
    --ink-soft: #5c5c60;
    --rule: #9a9a9e;
  }
  * { margin: 0; padding: 0; box-sizing: border-box; }
  html, body {
    width: 1200px;
    height: 780px;
    overflow: hidden;
    background: var(--backdrop);
    font-family: "Open Sans", sans-serif;
  }
  .canvas {
    position: relative;
    width: 1200px;
    height: 780px;
  }
  .card {
    position: absolute;
    left: 358px;
    width: 452px;
    height: 251px;
    background: var(--card);
  }
  .card--front { top: 103px; }
  .card--back { top: 407px; }

  /* Wordmark */
  .wordmark {
    position: absolute;
    display: flex;
    flex-direction: column;
    align-items: center;
    color: var(--ink);
  }
  .wordmark__dot {
    border: 3px solid currentColor;
    border-radius: 50%;
  }
  .wordmark__name {
    font-weight: 400;
    text-transform: uppercase;
    white-space: nowrap;
  }
  .card--front .wordmark {
    top: 32px;
    right: 30px;
  }
  .card--front .wordmark__dot {
    width: 30px;
    height: 30px;
    margin-bottom: 20px;
  }
  .card--front .wordmark__name {
    font-size: 11px;
    letter-spacing: 4px;
    margin-right: -4px;
  }
  .card--back .wordmark {
    top: 78px;
    left: 0;
    right: 0;
    color: var(--ink-strong);
  }
  .card--back .wordmark__dot {
    width: 46px;
    height: 46px;
    border-width: 4px;
    margin-bottom: 22px;
  }
  .card--back .wordmark__name {
    font-size: 17px;
    letter-spacing: 8px;
    margin-right: -8px;
  }

  /* Holder */
  .holder {
    position: absolute;
    left: 33px;
    top: 125px;
  }
  .holder__name {
    font-size: 14px;
    font-weight: 700;
    color: var(--ink);
    text-transform: uppercase;
    line-height: 18px;
  }
  .holder__role {
    font-size: 10.5px;
    color: var(--ink-soft);
    line-height: 13px;
  }
  .divider {
    position: absolute;
    left: 33px;
    right: 34px;
    top: 164px;
    height: 1px;
    background: var(--rule);
  }

  /* Contact */
  .contact {
    position: absolute;
    left: 34px;
    top: 178px;
    list-style: none;
  }
  .contact__item {
    display: flex;
    align-items: center;
    gap: 6px;
    height: 12.6px;
    font-size: 10.3px;
    color: var(--ink-soft);
  }
  .contact__icon {
    width: 8px;
    height: 8px;
    fill: var(--ink-soft);
    flex: none;
  }
  .social-handle {
    position: absolute;
    right: 33px;
    top: 203px;
    font-size: 10.3px;
    line-height: 12.6px;
    color: var(--ink-soft);
  }
</style>
</head>
<body>
<main class="canvas">

  <section class="card card--front" aria-label="Business card front">
    <div class="wordmark">
      <span class="wordmark__dot"></span>
      <span class="wordmark__name">Tallowfern Studio</span>
    </div>

    <div class="holder">
      <p class="holder__name">Derek Holloway</p>
      <p class="holder__role">Director</p>
    </div>

    <div class="divider"></div>

    <ul class="contact">
      <li class="contact__item">
        <svg class="contact__icon" viewBox="0 0 16 16" aria-hidden="true"><path d="M3.5 1l3 3-1.6 1.8c.9 1.9 2.4 3.4 4.3 4.3L11 8.5l3 3-2 2.5C6.5 13.5 2.5 9.5 1 3.5z"/></svg>
        <span>027.461.9037</span>
      </li>
      <li class="contact__item">
        <svg class="contact__icon" viewBox="0 0 16 16" aria-hidden="true"><path d="M1 3h14v1.2L8 9 1 4.2zM1 6l7 4.8L15 6v7H1z"/></svg>
        <span>info@tallowfernstudio.co.nz</span>
      </li>
      <li class="contact__item">
        <svg class="contact__icon" viewBox="0 0 16 16" aria-hidden="true"><path d="M8 1a7 7 0 100 14A7 7 0 008 1zm0 1.5c.8 0 1.7 1.5 2 4H6c.3-2.5 1.2-4 2-4zM2.6 6.5h2c-.1 1-.1 2 0 3h-2a5.6 5.6 0 010-3zm3.4 0h4a13 13 0 010 3H6a13 13 0 010-3zm5.4 0h2a5.6 5.6 0 010 3h-2c.1-1 .1-2 0-3zM6 11h4c-.3 2-1.2 3.5-2 3.5S6.3 13 6 11z"/></svg>
        <span>www.tallowfernstudio.co.nz</span>
      </li>
    </ul>

    <p class="social-handle">@tallowfernstudio</p>
  </section>

  <section class="card card--back" aria-label="Business card back">
    <div class="wordmark">
      <span class="wordmark__dot"></span>
      <span class="wordmark__name">Tallowfern Studio</span>
    </div>
  </section>

</main>
</body>
</html>
```